Residential Remodeling Contractor needs updated business card

I need a new design for my business card.
Name of the company is Brookfell Construction. I need a card that commands presence, strength, integrity. I have been in business for 28 years. I am a Residential Remodeling Contractor that covers all aspects of a residential remodel and build.

```html
<!DOCTYPE html>
<html lang="en">
<head>
<meta charset="utf-8">
<title>Brookfell Construction – Business Card</title>
<link href="https://fonts.googleapis.com/css2?family=Montserrat:wght@300;400;700&display=swap" rel="stylesheet">
<style>
  :root {
    --backdrop: #9a9a9a;
    --navy: #1f3d7c;
    --navy-deep: #1a356f;
    --paper: #ffffff;
    --ghost: #f2f2f2;
    --ink-muted: #6a6a6a;
    --ink-soft: #5b6fa3;
  }
  * { margin: 0; padding: 0; box-sizing: border-box; }
  html, body {
    width: 1200px; height: 1200px; overflow: hidden;
    background: var(--backdrop);
    font-family: "Montserrat", sans-serif;
  }
  .card {
    position: absolute;
    left: 226px;
    width: 746px; height: 436px;
    border-radius: 30px;
    overflow: hidden;
  }
  .card--front { top: 130px; background: var(--navy); }
  .card--back  { top: 639px; background: var(--paper); }

  .brand-mark {
    position: absolute;
    left: 0; right: 0; top: 162px;
    text-align: center;
    color: var(--navy-deep);
    font-weight: 700;
    text-transform: uppercase;
    line-height: 1.15;
  }
  .brand-mark__name { display: block; font-size: 50px; letter-spacing: 2px; }
  .brand-mark__trade { display: block; font-size: 30px; letter-spacing: 6px; }

  .brand-ghost {
    position: absolute;
    left: 46px; top: 24px;
    width: 168px; height: 412px;
    background: linear-gradient(to bottom, rgba(242,242,242,0) 0%, var(--ghost) 25%, var(--ghost) 100%);
  }

  .contact {
    position: absolute;
    right: 56px; top: 276px;
    text-align: right;
  }
  .contact__name {
    font-size: 16px; font-weight: 700; letter-spacing: 1.5px;
    color: var(--navy); text-transform: uppercase;
  }
  .contact__role {
    font-size: 16px; font-weight: 300; letter-spacing: 1px;
    color: var(--ink-soft); margin-top: 2px;
  }
  .contact__list { list-style: none; margin-top: 20px; }
  .contact__item {
    display: flex; justify-content: flex-end; align-items: center; gap: 10px;
    font-size: 16px; font-weight: 400; letter-spacing: 0.5px;
    color: var(--ink-muted); height: 25px;
  }
  .contact__icon { width: 15px; height: 15px; fill: var(--navy); flex: none; }
</style>
</head>
<body>
  <section class="card card--front">
    <div class="brand-mark">
      <span class="brand-mark__name">Brookfell</span>
      <span class="brand-mark__trade">Construction</span>
    </div>
  </section>

  <section class="card card--back">
    <div class="brand-ghost" role="img" aria-label="Faint brand decoration area"></div>
    <div class="contact">
      <p class="contact__name">Name Surname</p>
      <p class="contact__role">Position</p>
      <ul class="contact__list">
        <li class="contact__item">123-456-7890
          <svg class="contact__icon" viewBox="0 0 16 16" aria-hidden="true"><path d="M4 0h8a1 1 0 0 1 1 1v14a1 1 0 0 1-1 1H4a1 1 0 0 1-1-1V1a1 1 0 0 1 1-1zm1 2v10h6V2zm3 11a1 1 0 1 0 0 2 1 1 0 0 0 0-2z"/></svg>
        </li>
        <li class="contact__item">email@website.com
          <svg class="contact__icon" viewBox="0 0 16 16" aria-hidden="true"><path d="M0 3h16v10H0zm1.5 1.2v.3L8 9l6.5-4.5v-.3zM1 5.8V12h14V5.8L8 10.6z"/></svg>
        </li>
        <li class="contact__item">www.website.com
          <svg class="contact__icon" viewBox="0 0 16 16" aria-hidden="true"><path d="M8 1a7 7 0 1 0 0 14A7 7 0 0 0 8 1zm0 1.3c.8.8 1.4 2.2 1.6 3.7H6.4C6.6 4.5 7.2 3.1 8 2.3zM2.4 7h2.9c0 .7 0 1.3.1 2H2.4a5.6 5.6 0 0 1 0-2zm4 0h3.2a9 9 0 0 1 0 2H6.4a9 9 0 0 1 0-2zm4.3 0h2.9a5.6 5.6 0 0 1 0 2h-2.9c.1-.7.1-1.3 0-2zM6.4 10h3.2c-.2 1.5-.8 2.9-1.6 3.7-.8-.8-1.4-2.2-1.6-3.7z"/></svg>
        </li>
      </ul>
    </div>
  </section>
</body>
</html>
```